Online-Marketing-Material für Reinigungsbetrieb
Zielgruppe
Wir sind ein Reinigungsbetrieb mit den Schwerpunkten Treppenhausreinigung und Büroreinigung. Die Zielgruppe sind bei dieser Anzeige Unternehmer.
Aufgabenstellung
Wir wollen eine Aktion starten. 20 Prozent Neukundenrabatt auf Büroreinigungen. Wir sind ein junges, modernes Unternehmen, dass so auch dementsprechend rüber kommen soll.
Gerne mit unseren Farben.

```html
<!DOCTYPE html>
<html lang="de">
<head>
<meta charset="utf-8">
<title>Lippe Glanz – Cleaning Service</title>
<link rel="stylesheet" href="https://fonts.googleapis.com/css2?family=Rubik+Mono+One&family=Titan+One&family=Montserrat:wght@400;500&display=swap">
<style>
  :root {
    --tile-green: #72bf44;
    --grout: #b9d8e3;
    --floor: #a9d8d9;
    --brand-blue: #4a5fac;
    --box-blue: #3f56a9;
    --teal: #3dbfb0;
    --navy: #173c5c;
    --bubble: #a2d383;
    --white: #ffffff;
  }
  html, body { margin: 0; padding: 0; overflow: hidden; }
  body { width: 855px; height: 1200px; background: var(--tile-green); }
  .flyer { position: relative; width: 855px; height: 1200px; overflow: hidden; background: var(--tile-green); }
  .tiles { position: absolute; inset: 0; }
  .floor { position: absolute; left: 0; top: 1074px; width: 855px; height: 126px; background: var(--floor); }

  .brand { position: absolute; left: 88px; top: 30px; display: flex; align-items: center; gap: 12px; }
  .brand-square { width: 34px; height: 34px; background: var(--brand-blue); }
  .brand-name { font-family: "Titan One", sans-serif; font-size: 30px; line-height: 1; color: var(--brand-blue); }
  .brand-owner { position: absolute; left: 134px; top: 72px; font-family: "Montserrat", sans-serif; font-size: 10px; color: var(--teal); }

  .headline { position: absolute; left: 0; top: 0; width: 855px; height: 320px; }
  .headline text { font-family: "Rubik Mono One", sans-serif; fill: var(--brand-blue); }

  .tag { position: absolute; background: var(--teal); border-radius: 10px; color: var(--white);
         font-family: "Titan One", sans-serif; display: flex; align-items: center; justify-content: center; }
  .tag-claim { left: 64px; top: 362px; width: 387px; height: 76px; font-size: 23px; }
  .tag-service { left: 64px; width: 277px; height: 48px; font-size: 21px; }
  .tag-office { top: 504px; }
  .tag-stairs { top: 728px; }

  .highlights { position: absolute; left: 66px; margin: 0; padding: 0; list-style: none;
                font-family: "Montserrat", sans-serif; font-size: 15px; letter-spacing: 1px; color: var(--navy); }
  .highlights li { position: relative; height: 32.7px; padding-left: 37px; display: flex; align-items: center; }
  .highlights svg { position: absolute; left: 0; top: 6px; }
  .list-office { top: 562px; }
  .list-stairs { top: 785px; }

  .offer { position: absolute; left: 0; top: 0; width: 855px; height: 1200px; pointer-events: none; }
  .offer text { font-family: "Rubik Mono One", sans-serif; fill: var(--navy); }

  .illustration { position: absolute; left: 358px; top: 553px; width: 432px; height: 530px;
                  border-radius: 14px;
                  background: linear-gradient(180deg, rgba(48,144,210,0.55) 0%, #1b4a6c 45%, #123856 100%); }

  .address-box { position: absolute; left: 63px; top: 956px; width: 278px; height: 122px;
                 background: var(--box-blue); border-radius: 6px; color: var(--white); text-align: center; }
  .address-name { margin: 28px 0 0; font-family: "Rubik Mono One", sans-serif; font-size: 24px; letter-spacing: -0.5px; }
  .address-line { margin: 10px 0 0; font-family: "Montserrat", sans-serif; font-size: 12.5px; letter-spacing: 0.3px; }
</style>
</head>
<body>
<main class="flyer">
  <svg class="tiles" width="855" height="1200" aria-hidden="true">
    <g stroke="var(--grout)" stroke-width="1.2">
      <line x1="101.5" y1="0" x2="101.5" y2="1074"/>
      <line x1="210.5" y1="0" x2="210.5" y2="1074"/>
      <line x1="319" y1="0" x2="319" y2="1074"/>
      <line x1="427.5" y1="0" x2="427.5" y2="1074"/>
      <line x1="536" y1="0" x2="536" y2="1074"/>
      <line x1="644.5" y1="0" x2="644.5" y2="1074"/>
      <line x1="753" y1="0" x2="753" y2="1074"/>
      <line x1="0" y1="40.5" x2="855" y2="40.5"/>
      <line x1="0" y1="142" x2="855" y2="142"/>
      <line x1="0" y1="244" x2="855" y2="244"/>
      <line x1="0" y1="345" x2="855" y2="345"/>
      <line x1="0" y1="447" x2="855" y2="447"/>
      <line x1="0" y1="549" x2="855" y2="549"/>
      <line x1="0" y1="650" x2="855" y2="650"/>
      <line x1="0" y1="752" x2="855" y2="752"/>
      <line x1="0" y1="853" x2="855" y2="853"/>
      <line x1="0" y1="955" x2="855" y2="955"/>
      <line x1="0" y1="1057" x2="855" y2="1057"/>
    </g>
  </svg>
  <div class="floor"></div>

  <div class="brand">
    <span class="brand-square"></span>
    <span class="brand-name">Lippe Glanz</span>
  </div>
  <div class="brand-owner">Inh. Marco Albers</div>

  <svg class="headline" width="855" height="320">
    <text x="68" y="224" font-size="118" textLength="715" lengthAdjust="spacingAndGlyphs">CLEANING</text>
    <text x="67" y="303" font-size="72" textLength="381" lengthAdjust="spacingAndGlyphs">SERVICE</text>
  </svg>

  <div class="tag tag-claim">Zuverlässig, Professionell</div>

  <div class="tag tag-service tag-office">Büroreinigung</div>
  <ul class="highlights list-office">
    <li><svg width="16" height="22" viewBox="0 0 16 22"><path d="M3 2 L13 11 L3 20" fill="none" stroke="var(--navy)" stroke-width="3"/></svg>HIGHLITE 1</li>
    <li><svg width="16" height="22" viewBox="0 0 16 22"><path d="M3 2 L13 11 L3 20" fill="none" stroke="var(--navy)" stroke-width="3"/></svg>HIGHLITE 2</li>
    <li><svg width="16" height="22" viewBox="0 0 16 22"><path d="M3 2 L13 11 L3 20" fill="none" stroke="var(--navy)" stroke-width="3"/></svg>HIGHLITE 3</li>
    <li><svg width="16" height="22" viewBox="0 0 16 22"><path d="M3 2 L13 11 L3 20" fill="none" stroke="var(--navy)" stroke-width="3"/></svg>HIGHLITE 4</li>
  </ul>

  <div class="tag tag-service tag-stairs">Treppenhaus</div>
  <ul class="highlights list-stairs">
    <li><svg width="16" height="22" viewBox="0 0 16 22"><path d="M3 2 L13 11 L3 20" fill="none" stroke="var(--navy)" stroke-width="3"/></svg>HIGHLITE 1</li>
    <li><svg width="16" height="22" viewBox="0 0 16 22"><path d="M3 2 L13 11 L3 20" fill="none" stroke="var(--navy)" stroke-width="3"/></svg>HIGHLITE 2</li>
    <li><svg width="16" height="22" viewBox="0 0 16 22"><path d="M3 2 L13 11 L3 20" fill="none" stroke="var(--navy)" stroke-width="3"/></svg>HIGHLITE 3</li>
    <li><svg width="16" height="22" viewBox="0 0 16 22"><path d="M3 2 L13 11 L3 20" fill="none" stroke="var(--navy)" stroke-width="3"/></svg>HIGHLITE 4</li>
  </ul>

  <div class="illustration" role="img" aria-label="Illustration: Putzeimer mit Besen, Pümpel, Abzieher und Gummihandschuh, daneben zwei Reinigungsmittelflaschen"></div>

  <svg class="offer" width="855" height="1200">
    <circle cx="607" cy="391" r="146" fill="var(--bubble)" stroke="var(--white)" stroke-width="2"/>
    <g transform="rotate(-6 607 391)">
      <text x="607" y="318" font-size="19" text-anchor="middle">NEUKUNDEN</text>
      <text x="607" y="376" font-size="48" text-anchor="middle">20%</text>
      <text x="615" y="420" font-size="21" text-anchor="middle">RABATT AUF</text>
      <text x="620" y="452" font-size="23" text-anchor="middle">BÜROREINIGUNG</text>
    </g>
    <g fill="rgba(162,211,131,0.6)" stroke="var(--white)" stroke-width="1.3">
      <circle cx="735" cy="333" r="12"/>
      <circle cx="754" cy="496" r="21"/>
      <circle cx="436" cy="567" r="30"/>
    </g>
  </svg>

  <div class="address-box">
    <p class="address-name">LIPPE GLANZ</p>
    <p class="address-line">Birkenallee 17, 33175 Musterdorf</p>
  </div>
</main>
</body>
</html>
```